Website Navigation Redesign

We are looking for a redesign of the navigation system of our website. We prefer a clean, simple, modern look.
We are looking for three elements:
1. A top level navigation that jumps between 4 subdomains: Wealth Management, Direct Indexing, Ethical Investing and Superannuation
2. A secondary navigation for each subdomain similar to the one on this page: https://parcelfolio.au/ . The elements will be (a) 3-5 menu items (b) the ability to have submenus (c) a logo (d) a login button (e) a "call-to-action" button
3. A standard footer. See the footer from https://kestrelvault.com/ for the content to be included in the footer.
Each of the sub domains have very similar logos that we also want displayed (see uploaded image)
We are looking for 1 web page version and 1 mobile version.
It will be hosted on Hubspot CMS, and so solutions that will fit easily into that solution without custom coding will be preferred.
Our typical fonts are Ubuntu and Roboto. We prefer solutions using those fonts
Thanks
Target Market(s)
Small investors
Industry/Entity Type
Financial Services
Coding
Coded - Design and coding required
Number of Pages Required
1 page

```html
<!DOCTYPE html>
<html lang="en">
<head>
<meta charset="utf-8">
<title>Kestrel Vault – Navigation</title>
<link href="https://fonts.googleapis.com/css2?family=Poppins:wght@400;500;600;700&display=swap" rel="stylesheet">
<style>
:root{
  --black:#000;
  --white:#fff;
  --accent:#2aa8cf;
  --accent-text:#1a8fd6;
  --ink:#111;
  --rule:#d9d9d9;
}
*{margin:0;padding:0;box-sizing:border-box}
html,body{width:1200px;height:833px;overflow:hidden;background:var(--white);font-family:"Poppins",sans-serif;color:var(--ink)}
.page{position:relative;width:1200px;height:833px}
a{color:inherit;text-decoration:none}

.site-switcher{position:absolute;left:0;top:0;width:1200px;height:47px;background:var(--black);color:var(--white);font-size:11.5px;font-weight:700;letter-spacing:.1px}
.site-switcher .home{position:absolute;left:33px;top:15px}
.site-switcher .site{position:absolute;top:15px;width:208px;text-align:center}
.site-switcher .site.active{color:var(--accent-text)}
.site-switcher .divider{position:absolute;top:13px;width:1px;height:18px;background:var(--white)}

.main-nav{position:absolute;left:0;top:47px;width:1200px;height:85px}
.brand{position:absolute;left:58px;top:33px;display:flex;align-items:center;gap:5px;font-size:15px;font-weight:600;color:var(--ink)}
.brand .dot{width:9px;height:9px;border-radius:50%;background:var(--accent)}
.menu-item{position:absolute;top:34px;font-size:12.5px}
.menu-item.open{color:var(--accent-text)}
.menu-item.open svg{margin-left:6px;vertical-align:1px}
.login{position:absolute;left:967px;top:34px;font-size:12.5px;font-weight:600}
.cta{display:flex;align-items:center;justify-content:center;background:var(--accent);color:var(--white);font-weight:600;border-radius:18px;font-size:12px;text-align:center}
.main-nav .cta{position:absolute;left:1039px;top:26px;width:102px;height:34px}

.dropdown{position:absolute;left:197px;top:125px;width:523px;height:183px;background:var(--white);border-radius:0 0 8px 8px;box-shadow:0 3px 6px rgba(0,0,0,.18)}
.dropdown h2{position:absolute;left:26px;top:21px;font-size:21px;font-weight:600}
.dropdown p{position:absolute;left:26px;top:62px;width:268px;font-size:9.7px;line-height:15px;color:#222}
.dropdown ul{position:absolute;left:330px;top:6px;width:166px;list-style:none}
.dropdown li{height:37.5px;border-bottom:1px solid var(--rule);font-size:11.5px;font-weight:500;line-height:14px;padding:19px 0 0 3px}

.footer{position:absolute;left:0;top:420px;width:1200px;height:413px;background:var(--black);color:var(--white)}
.footer .col{position:absolute;top:50px}
.footer h3{font-size:13.5px;font-weight:600;margin-bottom:18px}
.footer .col a.link{display:block;font-size:12px;line-height:17.5px;margin-bottom:13.5px}
.footer .col a.cta{height:34px}
.footer-brand{position:absolute;left:107px;top:315px;display:flex;align-items:center;gap:6px;font-size:20px;font-weight:600}
.footer-brand .dot{width:11px;height:11px;border-radius:50%;background:var(--white)}
</style>
</head>
<body>
<div class="page">
  <nav class="site-switcher">
    <a class="home" href="#">KESTREL VAULT</a>
    <a class="site active" style="left:348px" href="#">DIRECT INDEXING</a>
    <span class="divider" style="left:555px"></span>
    <a class="site" style="left:556px" href="#">WEALTH MANAGEMENT</a>
    <span class="divider" style="left:763px"></span>
    <a class="site" style="left:765px" href="#">ETHICAL INVESTING</a>
    <span class="divider" style="left:972px"></span>
    <a class="site" style="left:972px" href="#">SUPERANNUATION</a>
  </nav>

  <header class="main-nav">
    <a class="brand" href="#"><span class="dot"></span>Kestrel</a>
    <a class="menu-item open" style="left:197px" href="#">Investments<svg width="9" height="6" viewBox="0 0 9 6"><path d="M0 6L4.5 0L9 6Z" fill="#1a8fd6"/></svg></a>
    <a class="menu-item" style="left:309px" href="#">Blogs</a>
    <a class="menu-item" style="left:366px" href="#">About us</a>
    <a class="menu-item" style="left:442px" href="#">Contact us</a>
    <a class="login" href="#">Login</a>
    <a class="cta" href="#">See my work</a>
  </header>

  <section class="dropdown">
    <h2>Investments</h2>
    <p>Direct Indexing helps small business owners like you save time and money doing your bookkeeping and income taxes by providing dedicated experts and easy-to-use financial software—so you can focus on growing your business.</p>
    <ul>
      <li>Link one</li>
      <li>Link two</li>
      <li>Link three</li>
      <li>Link four</li>
    </ul>
  </section>

  <footer class="footer">
    <div class="col" style="left:107px">
      <h3>Solutions</h3>
      <a class="link" href="#">Ethical Investing</a>
      <a class="link" href="#">Superannuation</a>
      <a class="link" href="#">Portfolios</a>
      <a class="link" href="#">Intermediaries</a>
    </div>
    <div class="col" style="left:307px">
      <h3>Company</h3>
      <a class="link" href="#">About Us</a>
      <a class="link" href="#">FAQs</a>
      <a class="link" href="#">Media</a>
      <a class="link" href="#">Privacy Policy</a>
      <a class="link" href="#">How we use your<br>information</a>
    </div>
    <div class="col" style="left:507px">
      <h3>Contact</h3>
      <a class="link" href="#">Level 3, 88 Harbour Lane<br>Melbourne Victoria 3000</a>
      <a class="link" href="#">1300 555 014</a>
      <a class="link" href="#">contact@kestrelvault.com</a>
      <a class="cta" style="width:160px;margin-top:22px" href="#">Book a Consultation</a>
    </div>
    <div class="col" style="left:715px">
      <h3>Latest Insights</h3>
      <a class="link" href="#">Housing Affordability Update |<br>Kestrel Investment Insights</a>
      <a class="link" href="#">Is the stock bubble about<br>to burst?</a>
      <a class="link" href="#">RBA rate cuts trigger house<br>price rebound</a>
    </div>
    <div class="col" style="left:948px">
      <h3>Invest With Us</h3>
      <a class="link" href="#">Member login</a>
      <a class="link" href="#" style="margin-bottom:16px">Leave us a review</a>
      <a class="cta" style="width:131px" href="#">Get Started</a>
    </div>
    <div class="footer-brand"><span class="dot"></span>Kestrel</div>
  </footer>
</div>
</body>
</html>
```